Veltrano - Mechanic/Collision Center Business Card

We're looking for a business card design for our mechanic/ collision repair shop.

Can be with colours or monochromatic.

See the attached files.

Many thanks

```html
<!DOCTYPE html>
<html lang="en">
<head>
<meta charset="utf-8">
<title>Veltrano Business Card</title>
<link rel="stylesheet" href="https://fonts.googleapis.com/css2?family=Work+Sans:wght@400;500;800&display=swap">
<style>
  :root {
    --stage: #1e1e1f;
    --card-dark: #222223;
    --card-light: #ffffff;
    --ink: #1f2326;
    --accent: #1e9ad8;
    --grey: #7a7b7e;
    --rule: #2a2a2a;
  }
  * { margin: 0; padding: 0; box-sizing: border-box; }
  html, body {
    width: 1200px; height: 900px; overflow: hidden;
    background: var(--stage);
    font-family: "Work Sans", Arial, sans-serif;
  }
  .card {
    position: absolute;
    width: 600px; height: 343px;
    left: 300px;
    overflow: hidden;
  }
  .card--back {
    top: 62px;
    background: var(--card-dark);
    display: flex; align-items: center; justify-content: center; gap: 14px;
  }
  .card--back .brand-dot {
    width: 22px; height: 22px; border-radius: 50%;
    background: var(--accent);
  }
  .card--back .brand-name {
    color: #ffffff;
    font-weight: 800; font-size: 54px;
    letter-spacing: 1px; text-transform: uppercase;
  }
  .card--front {
    top: 468px;
    background: var(--card-light);
    color: var(--ink);
  }
  .card--front .brand-name {
    position: absolute; right: 40px; top: 40px;
    font-weight: 800; font-size: 40px;
    letter-spacing: 1px; text-transform: uppercase;
    color: var(--ink);
  }
  .person { position: absolute; left: 58px; top: 118px; }
  .person__name {
    color: var(--accent); font-size: 27px; font-weight: 500;
    text-transform: uppercase; letter-spacing: 0.5px;
  }
  .person__role { font-size: 16px; margin-top: 2px; letter-spacing: 0.5px; }
  .contact {
    position: absolute; left: 58px; top: 196px;
    font-size: 15px; line-height: 23px; letter-spacing: 0.5px;
  }
  .contact .label, .contact .hl { color: var(--accent); }
  .address {
    position: absolute; left: 48px; top: 258px;
    font-size: 15px; letter-spacing: 0.5px;
  }
  .rule {
    position: absolute; left: 48px; right: 40px; top: 284px;
    height: 1px; background: var(--rule);
  }
  .band { position: absolute; left: 0; bottom: 0; width: 600px; height: 16px; }
</style>
</head>
<body>
  <section class="card card--back">
    <span class="brand-dot"></span>
    <span class="brand-name">Veltrano</span>
  </section>

  <section class="card card--front">
    <div class="brand-name">Veltrano</div>
    <div class="person">
      <div class="person__name">Daniel Reyes</div>
      <div class="person__role">Director</div>
    </div>
    <div class="contact">
      <div><span class="label">P:</span> 06.41.73.19.82 <span class="label">| E:</span> info@veltrano.com</div>
      <div><span class="label">W:</span> www.<span class="hl">veltrano</span>.com</div>
    </div>
    <div class="address">418 Maple Ridge Road, Harlow, PA 17230</div>
    <div class="rule"></div>
    <svg class="band" viewBox="0 0 600 16" preserveAspectRatio="none">
      <rect x="0" y="0" width="600" height="16" fill="var(--grey)"/>
      <polygon points="268,16 284,0 600,0 600,16" fill="var(--card-light)"/>
      <polygon points="276,16 290,4 600,4 600,16" fill="var(--accent)"/>
    </svg>
  </section>
</body>
</html>
```